Christmas Flyer for Suburban London Cocktail Bar & Party Venue

We need a flyer with details of our Christmas Party drinks packages for party bookings. Tin Lantern is a local cocktail bar with an emphasis on providing a modern hospitality environment with a sense of fun and whimsy. We pride ourselves on not being generic, providing a community atmosphere and don't take ourselves too seriously and our brand reflects that.

Christmas is one of the most popular times of year and we host parties for many people in our local area. The flyer is intended to summarise our promotional deals and will be distributed to local businesses as well as being available in the bar for customers.

An overview of our mood board that influences 'tone', as we await rebranding, can be seen at https://au.pinvaultex.com/derwickhaul/commercial-bar-fit-out-inspiration/

Target Market(s)

21-35 Urban Professionals

Industry/Entity Type

Hospitality

Colors

Designer to choose colors to be used in the design.

Requirements
Must have
• The 4 offers contained in the copy text. Can be adjusted for legibility as long as the offers remain substantively the same.
• The logo of the bar. The standard logo is the gold version however that can be recoloured if appropriate.
• The Address Tin Lantern - 47 Marrow Crescent - Balham, SE28 4QT - This need not be prominent.
Nice to have
• Our social media locations
• facebook /tinlanternbar
• Instagram /tinlanternbar
Should not have
• Should not contain photographs or exceptionally generic stock imagery.

```html
<!DOCTYPE html>
<html lang="en">
<head>
<meta charset="utf-8">
<title>Tin Lantern – Christmas Party Drinks Flyer</title>
<link href="https://fonts.googleapis.com/css2?family=Cinzel:wght@700;900&family=Oswald:wght@600&family=Roboto:wght@400&display=swap" rel="stylesheet">
<style>
  :root{
    --bg:#e9e6e2;
    --charcoal:#2c2c2d;
    --navy:#15264a;
    --navy-light:#1d3461;
    --red:#c4161c;
    --white:#ffffff;
    --silver:#d9d9d9;
  }
  *{box-sizing:border-box;margin:0;padding:0}
  html,body{width:1200px;height:675px;overflow:hidden;background:var(--bg)}
  .canvas{position:relative;width:1200px;height:675px}
  .page{position:absolute;top:28px;width:438px;height:620px;overflow:hidden;box-shadow:0 6px 18px rgba(0,0,0,.25)}

  /* ---------- front cover ---------- */
  .cover{left:140px;background:var(--charcoal)}
  .cover-art{position:absolute;inset:0}
  .cover-frame{position:absolute;inset:12px;border:1px solid rgba(255,255,255,.75);pointer-events:none}
  .brand{position:absolute;left:36px;top:50px;display:flex;align-items:center;gap:8px;
    font-family:"Cinzel",serif;font-weight:700;font-size:26px;color:var(--silver);letter-spacing:1px}
  .brand-dot{width:10px;height:10px;border-radius:50%;background:var(--silver)}
  .cover-tagline{position:absolute;right:34px;bottom:46px;text-align:right;
    font-family:"Cinzel",serif;font-weight:900;font-size:21px;line-height:1.45;color:var(--silver);font-variant:small-caps}
  .cover-address{position:absolute;left:24px;bottom:22px;font-family:"Roboto",sans-serif;font-size:7px;line-height:1.4;
    color:rgba(255,255,255,.7)}

  /* ---------- back: packages ---------- */
  .packages{left:622px;background:var(--charcoal)}
  .packages-title{position:absolute;left:0;right:0;top:18px;text-align:center;
    font-family:"Cinzel",serif;font-weight:900;font-size:21px;line-height:1.25;color:var(--white);font-variant:small-caps}
  .package{position:absolute;left:0;width:438px;height:128px}
  .package .photo{position:absolute;top:0;width:235px;height:112px;border:2px solid var(--white)}
  .package.text-left .photo{right:10px}
  .package.text-right .photo{left:10px}
  .package .info{position:absolute;top:4px;width:170px}
  .package.text-left .info{left:14px}
  .package.text-right .info{right:10px}
  .ribbon{background:var(--navy);color:var(--white);font-family:"Cinzel",serif;font-weight:700;font-size:11.5px;
    padding:4px 16px 4px 14px;clip-path:polygon(0 0,100% 0,94% 50%,100% 100%,0 100%,6% 50%);display:inline-block;font-variant:small-caps}
  .group-tag{display:block;width:max-content;margin:1px 0 0 40px;background:var(--white);color:var(--navy);
    font-family:"Roboto",sans-serif;font-size:6px;padding:0 4px;text-transform:uppercase}
  .items{list-style:none;margin-top:5px;font-family:"Roboto",sans-serif;font-size:7.5px;line-height:1.4;color:var(--silver);
    display:flex;flex-wrap:wrap}
  .items li{width:100%;white-space:nowrap}
  .items li.half{width:50%}
  .items li::before{content:"✓ ";color:var(--white)}
  .price{margin-top:6px;position:relative;height:44px}
  .price-oval{position:absolute;left:49px;top:0;width:72px;height:26px;border-radius:50%;background:var(--navy);
    color:var(--white);font-family:"Oswald",sans-serif;font-size:16px;text-align:center;line-height:26px}
  .saving{position:absolute;left:5px;top:24px;width:160px;height:18px;background:var(--red);color:var(--white);
    font-family:"Oswald",sans-serif;font-size:10px;letter-spacing:1.2px;text-align:center;line-height:18px;text-transform:uppercase;
    clip-path:polygon(0 0,100% 0,95% 50%,100% 100%,0 100%,5% 50%)}
</style>
</head>
<body>
<main class="canvas">

  <!-- front cover -->
  <section class="page cover">
    <svg class="cover-art" width="438" height="620" viewBox="0 0 438 620">
      <defs>
        <linearGradient id="barGradient" x1="0" y1="0" x2="0" y2="1">
          <stop offset="0" stop-color="#5a3a25"/>
          <stop offset=".35" stop-color="#7a5a44"/>
          <stop offset=".6" stop-color="#3b2a20"/>
          <stop offset="1" stop-color="#4a4a48"/>
        </linearGradient>
        <linearGradient id="navyGradient" x1="0" y1="0" x2="0" y2="1">
          <stop offset="0" stop-color="#1d3461"/>
          <stop offset="1" stop-color="#12213f"/>
        </linearGradient>
      </defs>
      <g role="img" aria-label="Photograph of the bar interior: timber ceiling, pendant lamps, brick wall and a rustic wooden bar counter">
        <rect width="438" height="620" fill="url(#barGradient)"/>
      </g>
      <polygon points="0,0 300,0 0,440" fill="var(--charcoal)"/>
      <polygon points="438,190 438,620 150,620" fill="url(#navyGradient)"/>
    </svg>
    <div class="cover-frame"></div>
    <div class="brand"><span class="brand-dot"></span>Tin Lantern</div>
    <p class="cover-tagline">Modern<br>Hospitality<br>Environment<br>With A Sense Of<br>Fun And Whimsy</p>
    <p class="cover-address">Tin Lantern · 47 Marrow Crescent · Balham, SE28 4QT<br>facebook /tinlanternbar · instagram /tinlanternbar</p>
  </section>

  <!-- back: packages -->
  <section class="page packages">
    <h1 class="packages-title">Christmas Party Drinks<br>Packages For Party Bookings</h1>

    <article class="package text-left" style="top:84px">
      <div class="photo" role="img" aria-label="Photograph of a large sharing cocktail in front of a back bar of bottles" style="background:linear-gradient(135deg,#8a3a1e,#c9843e 50%,#3a2417)"></div>
      <div class="info">
        <span class="ribbon">Sharing Combo</span>
        <ul class="items"><li>3 of our sharing cocktails</li><li>Bottle of prosecco</li></ul>
        <div class="price"><div class="price-oval">£85</div><div class="saving">Save up to £35</div></div>
      </div>
    </article>

    <article class="package text-right" style="top:212px">
      <div class="photo" role="img" aria-label="Photograph of a large sharing cocktail in front of a back bar of bottles" style="background:linear-gradient(135deg,#3a2417,#c9843e 50%,#8a3a1e)"></div>
      <div class="info">
        <span class="ribbon">Xmas Package 1</span>
        <span class="group-tag">10 people</span>
        <ul class="items"><li class="half">10x Cocktails</li><li class="half">10x Beers</li><li>10x house spirit + mixer</li><li>Bottle of prosecco</li></ul>
        <div class="price"><div class="price-oval">£150</div><div class="saving">Save up to £85</div></div>
      </div>
    </article>

    <article class="package text-left" style="top:340px">
      <div class="photo" role="img" aria-label="Photograph of a large sharing cocktail in front of a back bar of bottles" style="background:linear-gradient(135deg,#8a3a1e,#c9843e 50%,#3a2417)"></div>
      <div class="info">
        <span class="ribbon">Xmas Package 2</span>
        <span class="group-tag">15 people</span>
        <ul class="items"><li class="half">15x Cocktails</li><li class="half">15x Beers</li><li>15x house spirit + mixer</li><li>Sharing cocktail</li></ul>
        <div class="price"><div class="price-oval">£220</div><div class="saving">Save up to £85</div></div>
      </div>
    </article>

    <article class="package text-right" style="top:468px">
      <div class="photo" role="img" aria-label="Photograph of a large sharing cocktail in front of a back bar of bottles" style="background:linear-gradient(135deg,#3a2417,#c9843e 50%,#8a3a1e)"></div>
      <div class="info">
        <span class="ribbon">Xmas Package 3</span>
        <span class="group-tag">20 people</span>
        <ul class="items"><li class="half">20x Cocktails</li><li class="half">20x Beers</li><li>20x house spirit + mixer</li><li class="half">Bottle of prosecco</li><li class="half">Treasure chest</li></ul>
        <div class="price"><div class="price-oval">£350</div><div class="saving">Save up to £100</div></div>
      </div>
    </article>
  </section>

</main>
</body>
</html>
```